Creative lead conversion landing page for SMBs

We have an AI chatbot webpage for a real estate agent, and we’re are going to start sending traffic to that webpage (primarily from Zintavo)
We want to maximize the percentage of visitors who start conversations with the chatbot.
We have a specific area of the webpage where we can include any HTML.
We need the design and HTML for both desktop and mobile version.
We’re looking for the best designs that help convert visitors into people who engage the chatbot.

Details are in the attached document "Pitchforge project for chat conversion". Please let me know if you have any questions!

Target Market(s)

SMBs (think real estate agents, or home services like tree care, housekeepers, electricians, general contractors) will be selling to consumers

Number of Pages Required

1 page

Font styles to use
Other font styles liked:
• Zintavo Poppins

Requirements
Must have
• Creative design that catches users eyes and with good content (content of course out of scope) will encourage a user to want to learn more.

```html
<!DOCTYPE html>
<html lang="en">
<head>
<meta charset="utf-8">
<title>Porchlight – Marisol, Real Estate Agent</title>
<link href="https://fonts.googleapis.com/css2?family=Poppins:wght@400;500;600;700;800&display=swap" rel="stylesheet">
<style>
  :root{
    --purple:#6556a8;
    --navy:#021730;
    --cyan:#22b0d3;
    --panel:#f1f1f1;
    --white:#ffffff;
    --ink:#0f1a2b;
    --body:#4d4d4d;
    --muted:#9a9a9a;
    --line:#e2e2e2;
    --green:#1ec232;
    --field:#ececec;
  }
  *{box-sizing:border-box;margin:0;padding:0}
  html,body{width:1152px;height:1200px;overflow:hidden}
  body{position:relative;font-family:"Poppins",sans-serif;background:var(--white);color:var(--ink)}

  .sidebar{position:absolute;left:0;top:0;width:314px;height:1110px;background:var(--panel)}
  .brand-bar{height:68px;background:var(--purple);display:flex;align-items:center;justify-content:center;color:var(--white);font-weight:600;font-size:26px}
  .avatar{position:absolute;left:84px;top:108px;width:146px;height:146px;border-radius:50%;border:2px solid var(--green);padding:5px}
  .avatar-photo{width:100%;height:100%;border-radius:50%;background:radial-gradient(circle at 50% 45%,#c9a58e 0,#8a6a58 45%,#2c221e 80%)}
  .status-dot{position:absolute;left:184px;top:229px;width:22px;height:22px;border-radius:50%;background:var(--green);border:3px solid var(--white)}
  .agent-name{position:absolute;left:0;width:314px;top:266px;text-align:center;font-weight:700;font-size:29px;line-height:40px}
  .agent-role{position:absolute;left:0;width:314px;top:304px;text-align:center;font-size:18px;color:var(--body);line-height:26px}
  .agent-bio{position:absolute;left:44px;width:226px;top:337px;text-align:center;font-size:12px;line-height:20px;color:var(--body)}
  .assistant-cta{position:absolute;left:0;width:314px;top:444px;text-align:center;font-size:15px;font-weight:500;color:var(--cyan)}
  .pill{position:absolute;left:31px;width:251px;height:42px;border-radius:21px;display:flex;align-items:center;justify-content:center;color:var(--white);font-weight:700;font-size:14px}
  .pill-navy{top:479px;background:var(--navy)}
  .pill-purple{top:536px;background:var(--purple)}
  .pill-cyan{top:593px;background:var(--cyan)}

  .topic-card{position:absolute;width:380px;height:59px;border:1px solid var(--line);border-radius:8px;padding:10px 14px}
  .topic-title{display:flex;align-items:center;gap:6px;font-weight:600;font-size:13.5px;line-height:20px}
  .topic-title svg{width:12px;height:12px}
  .topic-desc{font-size:11px;color:var(--muted);margin-top:2px}

  .bot-bubble{position:absolute;left:347px;width:408px;background:var(--white);border-radius:8px;box-shadow:0 2px 10px rgba(0,0,0,.08);padding:16px 19px;font-size:15px;line-height:26px;color:var(--body)}
  .bubble-tail{position:absolute;left:397px;top:938px}
  .user-bubble{position:absolute;left:982px;top:797px;width:139px;height:42px;border-radius:8px;background:var(--purple);color:var(--white);font-size:15px;font-weight:500;display:flex;align-items:center;justify-content:center;box-shadow:0 3px 6px rgba(0,0,0,.12)}
  .mascot{position:absolute;left:347px;top:949px;width:55px;height:69px;border-radius:45% 45% 30% 30%;background:linear-gradient(#8dd8e4,#4fb8cc)}

  .composer{position:absolute;left:332px;top:1034px;width:789px;height:52px;border-radius:26px;background:var(--field);display:flex;align-items:center;padding-left:23px;font-size:17px;color:#8e8e8e}
  .send{position:absolute;right:5px;top:6px;width:40px;height:40px;border-radius:50%;background:var(--purple);display:flex;align-items:center;justify-content:center}

  .footer{position:absolute;left:0;top:1110px;width:1152px;height:90px;background:var(--navy)}
  .footer .pill{top:24px;background:var(--purple)}
  .footer-brand{position:absolute;right:30px;top:15px;text-align:right;color:var(--white);font-weight:600;font-size:24px;line-height:32px}
  .footer-note{position:absolute;right:30px;top:52px;font-size:11px;color:#8b93a3;font-weight:500}
</style>
</head>
<body>
  <aside class="sidebar">
    <div class="brand-bar">Porchlight</div>
    <div class="avatar"><div class="avatar-photo" role="img" aria-label="Portrait photo of the agent"></div></div>
    <div class="status-dot"></div>
    <h1 class="agent-name">Marisol</h1>
    <p class="agent-role">Real Estate Agent</p>
    <p class="agent-bio">Lorem ipsum dolor sit amet, sectetur adipiscing elit, sed ist do eiusmod tempor incididunt ut labore et dolore magna aliqua.</p>
    <p class="assistant-cta">Talk To Wren, My AI Assistant.</p>
    <div class="pill pill-navy">Search For Real Estate</div>
    <div class="pill pill-purple">Things To Do In Indianapolis</div>
    <div class="pill pill-cyan">My Review</div>
  </aside>

  <div class="topic-card" style="left:347px;top:31px">
    <div class="topic-title"><svg viewBox="0 0 12 12" fill="none" stroke="#0f1a2b" stroke-width="1.2"><circle cx="6" cy="4" r="2.3"/><path d="M1.5 11c0-2.5 2-3.8 4.5-3.8S10.5 8.5 10.5 11z"/></svg>Biographical Info</div>
    <p class="topic-desc">Lorem ipsum dolor sit amet consectetur adipiscing elit.</p>
  </div>
  <div class="topic-card" style="left:741px;top:31px">
    <div class="topic-title"><svg viewBox="0 0 12 12" fill="none" stroke="#0f1a2b" stroke-width="1.2"><path d="M6 1l1.5 3.2 3.4.4-2.5 2.3.7 3.4L6 8.6 2.9 10.3l.7-3.4L1.1 4.6l3.4-.4z"/></svg>Client Reviews</div>
    <p class="topic-desc">Lorem ipsum dolor sit amet consectetur adipiscing elit.</p>
  </div>
  <div class="topic-card" style="left:347px;top:105px">
    <div class="topic-title"><svg viewBox="0 0 12 12" fill="none" stroke="#0f1a2b" stroke-width="1.2"><rect x="1" y="1" width="10" height="10"/><path d="M1 9l3.5-3.5L11 11M7 5l4-4"/></svg>Related Pictures</div>
    <p class="topic-desc">Lorem ipsum dolor sit amet consectetur adipiscing elit.</p>
  </div>
  <div class="topic-card" style="left:741px;top:105px">
    <div class="topic-title"><svg viewBox="0 0 12 12" fill="none" stroke="#0f1a2b" stroke-width="1.2"><path d="M4 6V2a1 1 0 0 1 2 0v3.5M6 5a1 1 0 0 1 2 0v1M8 6a1 1 0 0 1 2 0v2.5C10 10 9 11 7.5 11H6C4.5 11 3 9.5 2.5 8L2 7a1 1 0 0 1 2-.5"/></svg>Help Me Pick</div>
    <p class="topic-desc">Lorem ipsum dolor sit amet consectetur adipiscing elit.</p>
  </div>

  <div class="bot-bubble" style="top:650px">Hi! I'm the AI assistant to Marisol, who can help you buy or sell a home in the Indianapolis area. I am happy to help get you connected to her. First, what's your name?</div>
  <div class="user-bubble">Johnathan</div>
  <div class="bot-bubble" style="top:855px">Hi Johnathan! It's great to meet you. How can I assist you today?</div>
  <svg class="bubble-tail" width="32" height="26" viewBox="0 0 32 26"><path d="M4 0h28L0 26z" fill="#ffffff"/></svg>
  <div class="mascot" role="img" aria-label="Assistant mascot character"></div>

  <div class="composer">Type Your Message...
    <div class="send"><svg width="20" height="18" viewBox="0 0 20 18"><path d="M1 1l18 8-18 8 3-8z" fill="#ffffff"/><path d="M4 9h8" stroke="#6556a8" stroke-width="1.5"/></svg></div>
  </div>

  <footer class="footer">
    <div class="pill">Create Your Own Free Wren</div>
    <div class="footer-brand">Porchlight</div>
    <div class="footer-note">Wren Uses AI and Can Make Mistakes</div>
  </footer>
</body>
</html>
```